Fold up small biz card size flyer for Waxing Salon

To design a simple informative flyer which can fold 3 times measuring 2" x 9" for Waxing Salon in Toronto ON CanadaMy client would like both sides of flyer to have text i.e. the first half of flyer text on front and second half with address etc on back.She doesn;t want a company name as yet but would like maybe the simple shape of a body as in this sample deisign with a stone background.the other pics are just samples of ideas she has suggessted and if there is any text it should simply be wax or waxing or maybe body waxing.Please don't hesitate to ask quesition and i look forward to your submissions.

Target Market(s)

women amd men of all adult ages

Font styles to use
Serif
Sans Serif
Decorative
Script

Colors

Designer to choose colors to be used in the design.

Requirements
Must have
• Fold into three to biz card size so PLEASE STRICTLY 2 INCHES X 9 INCHES AND FOLDED DOWN TO A 2 X 3 BIZ CARD
• Due to small size of flyer there will have to be text on back as well
• thanks for your time and patience
Nice to have
• the images are simply ideas of existing brands...just stone background with perhadps small body shaped graphic no company name
Should not have
• scanitly clad women preferably small body shoped graphic only please/

```html
<!DOCTYPE html>
<html lang="en">
<head>
<meta charset="utf-8">
<title>Body Waxing Fold-Up Flyer</title>
<link href="https://fonts.googleapis.com/css2?family=Montserrat:wght@400;600;700&family=Playfair+Display:wght@400;700&family=Great+Vibes&display=swap" rel="stylesheet">
<style>
:root{
  --board:#e4e3e1;
  --mauve:#c2948d;
  --mauve-dark:#a9776f;
  --blush:#ef9c99;
  --blush-soft:#f6d3cf;
  --white:#ffffff;
  --ink:#5b4a47;
  --guide:#7a7a7a;
}
*{margin:0;padding:0;box-sizing:border-box}
html,body{width:853px;height:1200px;overflow:hidden}
body{background:var(--board);font-family:'Montserrat',sans-serif;color:var(--ink);position:relative}
.size-label{position:absolute;top:18px;width:175px;text-align:center;font-size:11px;line-height:1.3;color:var(--guide)}
.size-label--outside{left:92px}
.size-label--inside{left:312px}
.panel-label{position:absolute;left:48px;font-size:11px;color:var(--guide);transform:rotate(-90deg);transform-origin:left top;white-space:nowrap}
.fold-line{position:absolute;left:60px;width:470px;border-top:1px dashed var(--guide)}
.strip{position:absolute;top:58px;width:175px;height:1090px;box-shadow:0 3px 10px rgba(0,0,0,.18);overflow:hidden}
.strip--outside{left:92px;background:var(--white)}
.strip--inside{left:312px;background:var(--mauve);color:var(--white)}
.photo{position:absolute;left:0;width:100%}
.btn{position:absolute;left:14px;right:14px;height:20px;background:var(--blush);color:var(--white);font-size:7px;font-weight:700;letter-spacing:.5px;display:flex;align-items:center;justify-content:center;border-radius:10px}
.deal{position:absolute;left:0;right:0;padding:0 10px}
.deal__title{background:var(--blush);color:var(--white);font-size:10px;font-weight:700;padding:4px 6px;margin-bottom:5px}
.deal__text{font-size:6.5px;line-height:1.45}
.deal__lead{font-size:8px;font-weight:700;margin-bottom:3px}
.back-panel{position:absolute;left:0;right:0;top:707px;bottom:0;background:var(--mauve);color:var(--white);text-align:center}
.script{font-family:'Great Vibes',cursive;font-size:21px;line-height:1.1}
.address{font-size:7px;line-height:1.5;margin-top:12px}
.headline{font-family:'Playfair Display',serif;font-weight:700;font-size:19px;text-align:center;line-height:1.15}
.offer{margin:8px auto 5px;width:130px;background:var(--blush-soft);color:var(--mauve-dark);font-size:9px;font-weight:700;text-align:center;padding:4px 0}
.offer-note{font-size:6.5px;text-align:center;padding:0 16px;line-height:1.4}
.services{position:absolute;left:20px;right:10px;list-style:none;font-size:9.5px;line-height:15.6px}
.note{position:absolute;left:0;right:0;top:940px;text-align:center}
.note__text{font-size:7px;line-height:1.5;margin-top:4px}
</style>
</head>
<body>
<div class="size-label size-label--outside">outside<br>2" x 9"</div>
<div class="size-label size-label--inside">inside<br>2" x 9"</div>
<div class="panel-label" style="top:260px">front</div>
<div class="panel-label" style="top:605px">back</div>
<div class="panel-label" style="top:985px">last fold 2" x 3"</div>
<div class="fold-line" style="top:410px"></div>
<div class="fold-line" style="top:765px"></div>

<section class="strip strip--outside">
  <div class="photo" role="img" aria-label="Simple line shape of a body outline" style="top:0;height:70px;background:linear-gradient(#fff,#f7eeed)"></div>
  <div class="photo" role="img" aria-label="Photo of a woman wrapped in a white towel" style="top:70px;height:200px;background:linear-gradient(160deg,#f4f1ef,#e6d6d1 55%,#f1e8e5)"></div>
  <div class="btn" style="top:305px">CALL TODAY TO BOOK A WAX</div>
  <div class="photo" role="img" aria-label="Photo of smooth waxed legs" style="top:352px;height:88px;background:linear-gradient(120deg,#ead3c8,#f6ebe6)"></div>
  <div class="deal" style="top:450px">
    <div class="deal__title">DOORBUSTER DEAL !</div>
    <div class="deal__lead">For women only!</div>
    <p class="deal__text">Book any wax treatment at our salon this month and enjoy a free bikini line add-on with any leg or arm wax. Offer valid on regular services only, one per client visit, ask for details.</p>
  </div>
  <div class="deal" style="top:555px">
    <div class="deal__title">BRAZILIAN WAX</div>
    <p class="deal__text">The secret to soft, smooth skin.</p>
  </div>
  <div class="photo" role="img" aria-label="Photo of legs after waxing" style="top:598px;height:75px;background:linear-gradient(110deg,#f4e9e4,#e2c8bd)"></div>
  <div class="btn" style="top:680px">CALL TODAY TO BOOK A WAX</div>
  <div class="back-panel">
    <p class="script" style="margin-top:28px">Smooth skin is<br>always in fashion</p>
    <p class="address">120 Maple Grove Ave<br>Toronto ON, M6K 1B2<br>Opp to Maple Grove Plaza<br>(416) 555-0142</p>
    <p class="address">48 Lakeshore Lane<br>Toronto ON, M1P 2R5<br>Opp to Lakeshore Mall<br>(647) 555-0199</p>
  </div>
</section>

<section class="strip strip--inside">
  <div role="img" aria-label="Round beauty photo of glowing skin" style="position:absolute;left:45px;top:14px;width:85px;height:85px;border-radius:50%;border:3px solid var(--white);background:radial-gradient(circle at 40% 40%,#f3dcd3,#d8b3a7)"></div>
  <div style="position:absolute;left:0;right:0;top:118px">
    <h1 class="headline">UNBEATABLE<br>VALUE !</h1>
    <div class="offer">$5 ON THE NEXT VISIT</div>
    <p class="offer-note">$10 each visit when you purchase 6 services or more from list below</p>
  </div>
  <ol class="services" style="top:370px">
    <li>1. Back Massage</li><li>2. Back Scrub</li><li>3. Spa Manicure</li><li>4. Full Brazilian Wax</li><li>5. Full 60 Minute Facial</li><li>6. Face Polishing</li><li>7. Face Bleaching</li><li>8. Scalp &amp; Hair Oil Massage</li><li>9. Dry Hair Treatment</li><li>10. Hair Colour Application</li><li>11. Four Inch Henna Tattoo</li><li>12. Eyebrow Tinting/Shaping</li><li>13. Upper Lip Thread/Wax</li><li>14. Forehead Thread/Wax</li><li>15. Side Burn Thread/Wax</li><li>16. Full Face Thread/Wax</li><li>17. Nostril Wax</li><li>18. Nape Wax</li>
  </ol>
  <ol class="services" style="top:722px">
    <li>19. Cleavage Wax</li><li>20. Stomach Wax</li><li>21. Lower Back Wax</li><li>22. Upper Back Wax</li><li>23. Underarm Wax</li><li>24. Half Arm Wax</li><li>25. Full Arm Wax</li><li>26. Half Leg Wax</li><li>27. Full Leg Wax</li><li>28. Bikini Line Wax</li><li>29. Bum Wax</li><li>30. Hollywood Wax</li>
  </ol>
  <div class="note">
    <p class="script">Note</p>
    <p class="note__text">$5 extra for nail polish<br>#6 counts as 2 services<br>#5 counts as 2 services</p>
  </div>
</section>
</body>
</html>
```